Label Design for American Pet Health Startup

We need your help in creating a line-up of labels for our upcoming products. The products will come in two different sizes/shapes. We have a logo (sourced form GraphiHive!) to start from and a pretty extensive brief (see attached.) The winning design will be bold, simple, and create a strongly branded look to the whole line while allowing consumers to easily sort through the different SKUs.

The logo and other existing design elements are in the attached powerpoint. I will also post some of the source files.

If you choose to compete for this project, please read the creative brief and the powerpoint very carefully before starting.

Thank you for your time and consideration.

Target Market(s)

Pet owners (dog owners, initially) who care deeply about their pets. Their pets are older and may not be thriving the way they once were. The owners want their pets to have the highest quality of life possible, for as long as is practical. They take their pets frequently to the vet and have great faith in veterinary medicine, but they also believe that dietary supplements may have a beneficial effect. They believe this to be possible because they take supplements themselves.

They are probably older--empty nesters or soon to be. They’ve owned their dog for five years or more, or have rescued an older dog from a shelter. Their dog is, in many ways, a full member of their family.

Industry/Entity Type

Pet Care

Font styles to use
Sans Serif

Requirements
Must have
• Please see the attached brief for this detail. I have cut and paste it into this form but it doesn't translate well. Reading the Word document will be easier and the links will work.
• Packaging Creative Considerations: The product packaging needs to . . .
• • Have a strong, branded line look.
• - The logo has already been developed, and I would like you to be guided in your design choices by its structure and color, but I am open to deviations from the existing work if it leads to a strong design
• • Use color or some other design elements to distinguish each SKU from the other
• • Be bold and simple. This product will typically be merchandised online, with very small images of the packaging. Simple and bold design elements will ensure that the products are both noticed and understood.
• - The product will likely be contained within white plastic or aluminum (silver) bottles with white caps/pumps. However, if you believe your design concepts would benefit from a particular color of bottle/container, please illustrate that, as that would be possible to execute.
• • Communicate that these products are for pets without using any clichés. This category is full of packaging with stock photos of dogs and cats. Please avoid this at all costs. Instead, please unleash your creativity to illustrate the products’ nature/purposes.
• A couple of packaging designs I would like you to draw inspiration from:
• o Vemo. This line is for human supplements/vitamins. Notice the strong line look, the simple and bold graphics, and the smart use of color and other design elements to differentiate the SKUs (while still holding it together as a single brand.)
• o Tundo. This line is for pets. Again, notice the strong line look, the smart use of color to differentiate the SKUs, and the simple and bold presentation that translates so well on the screen.
• o Corvalune. This design is not as good as the first two, but it does accomplish several of the brief’s objectives and the packaging is likely to be very similar to what your design will eventually be affixed to.
• Design Deliverables: A great submission will illustrate its strength by showing how the design translates across all the expected SKUs. To accomplish, this, I would recommend using the “functional maps” I’ve included in the attached Powerpoint document to:
• o First illustrate, in greater size and detail, one SKU each of the two families (one oil SKU and one supplement SKU)
• o Then illustrate how each of those designs extends across the rest of the family. That illustration can be less detailed. We just need to see how the colors and other design elements extend.
Should not have
• No stock images of cats or dogs; please avoid junking up the designs with too many elements

```html
<!DOCTYPE html>
<html lang="en">
<head>
<meta charset="utf-8">
<title>Wagmere Supplement Labels</title>
<link href="https://fonts.googleapis.com/css2?family=Oswald:wght@300;700&family=Lato:wght@400;700&display=swap" rel="stylesheet">
<style>
  :root {
    --teal: #17aebb;
    --orange: #f7941d;
    --ink: #141414;
    --paper: #ffffff;
    --backdrop: #cfcfcf;
    --brand-gray: #8a8d8f;
  }
  * { box-sizing: border-box; margin: 0; padding: 0; }
  html, body { width: 1200px; height: 900px; overflow: hidden; }
  body {
    background: var(--backdrop);
    position: relative;
    font-family: "Lato", sans-serif;
  }
  .label {
    position: absolute;
    top: 86px;
    width: 398px;
    height: 715px;
    background: var(--paper);
    overflow: hidden;
  }
  .label--salmon { left: 177px; --sku: var(--teal); }
  .label--omega { left: 618px; --sku: var(--orange); }

  .brand {
    position: absolute;
    top: 86px; left: 0; width: 100%;
    display: flex; justify-content: center; align-items: center; gap: 8px;
    font-family: "Lato", sans-serif;
    font-weight: 400;
    font-size: 30px;
    color: var(--brand-gray);
  }
  .brand__dot {
    width: 14px; height: 14px; border-radius: 50%;
    background: var(--brand-gray);
  }

  .kicker {
    position: absolute; left: 0; width: 100%;
    display: flex; justify-content: center; align-items: center;
    font-family: "Lato", sans-serif; font-weight: 700;
    color: var(--ink);
  }
  .kicker::before, .kicker::after {
    content: ""; height: 2px; background: var(--ink);
  }
  .label--salmon .kicker { top: 176px; font-size: 32px; letter-spacing: 14px; gap: 14px; }
  .label--salmon .kicker::before, .label--salmon .kicker::after { width: 70px; }
  .label--omega .kicker { top: 164px; font-size: 34px; letter-spacing: 3px; gap: 4px; }
  .label--omega .kicker::before, .label--omega .kicker::after { width: 70px; }

  .product-name {
    position: absolute; left: 0; width: 100%;
    text-align: center;
    font-family: "Oswald", sans-serif; font-weight: 700;
    color: var(--sku);
    line-height: 1;
    letter-spacing: -1px;
  }
  .label--salmon .product-name { top: 210px; font-size: 74px; }
  .label--omega .product-name { top: 190px; font-size: 104px; }

  .claim {
    position: absolute; left: 0; width: 100%;
    text-align: center;
    font-size: 19px; color: var(--ink);
  }
  .label--salmon .claim { top: 291px; }
  .label--omega .claim { top: 294px; }

  .color-field {
    position: absolute; left: 0; top: 337px;
    width: 398px; height: 378px;
  }
  .color-field path { fill: var(--sku); }

  .supplement {
    position: absolute; top: 395px; left: 0; width: 100%;
    text-align: center;
    font-family: "Oswald", sans-serif; font-weight: 300;
    font-size: 40px; color: var(--ink);
    letter-spacing: -1px;
  }
  .species {
    position: absolute; top: 455px; left: 0; width: 100%;
    display: flex; justify-content: center; align-items: center; gap: 18px;
  }
  .species__icon {
    width: 46px; height: 40px; border-radius: 50%;
    background: var(--ink);
  }
  .species__plus {
    font-family: "Lato", sans-serif; font-weight: 700;
    font-size: 28px; color: var(--ink);
  }
  .stripe {
    position: absolute; top: 546px; left: 0; width: 100%; height: 28px;
    background: var(--ink);
  }
  .seal {
    position: absolute; top: 512px; left: 153px;
    width: 92px; height: 92px; border-radius: 50%;
    background: var(--ink);
    border: 4px solid var(--sku);
    box-shadow: 0 0 0 2px var(--ink);
  }
  .seal::after {
    content: ""; position: absolute; inset: 18px;
    border-radius: 50%; background: var(--paper);
  }
  .net {
    position: absolute; top: 624px; left: 0; width: 100%;
    text-align: center;
    font-family: "Oswald", sans-serif; font-weight: 300;
    font-size: 25px; color: var(--ink);
    letter-spacing: -0.5px;
  }
</style>
</head>
<body>

  <section class="label label--salmon">
    <div class="brand"><span class="brand__dot"></span>Wagmere</div>
    <div class="kicker">PURE</div>
    <h1 class="product-name">SALMON OIL</h1>
    <p class="claim">SUPPORTS HEALTHY COAT &amp; SKIN</p>
    <svg class="color-field" viewBox="0 0 398 378" aria-hidden="true">
      <path d="M0,0 H150 C178,0 192,14 199,33 C206,14 220,0 248,0 H398 V378 H0 Z"/>
    </svg>
    <p class="supplement">ALL NATURAL SUPPLEMENT</p>
    <div class="species">
      <span class="species__icon" role="img" aria-label="Dog head icon"></span>
      <span class="species__plus">+</span>
      <span class="species__icon" role="img" aria-label="Cat head icon"></span>
    </div>
    <div class="stripe"></div>
    <div class="seal" role="img" aria-label="Ingredient seal"></div>
    <p class="net">Net 32 FL OZ / 946 ML</p>
  </section>

  <section class="label label--omega">
    <div class="brand"><span class="brand__dot"></span>Wagmere</div>
    <div class="kicker">FISH OIL</div>
    <h1 class="product-name">OMEGA 3</h1>
    <p class="claim">SUPPORTS HEALTHY COAT &amp; SKIN</p>
    <svg class="color-field" viewBox="0 0 398 378" aria-hidden="true">
      <path d="M0,0 H150 C178,0 192,14 199,33 C206,14 220,0 248,0 H398 V378 H0 Z"/>
    </svg>
    <p class="supplement">ALL NATURAL SUPPLEMENT</p>
    <div class="species">
      <span class="species__icon" role="img" aria-label="Dog head icon"></span>
      <span class="species__plus">+</span>
      <span class="species__icon" role="img" aria-label="Cat head icon"></span>
    </div>
    <div class="stripe"></div>
    <div class="seal" role="img" aria-label="Ingredient seal"></div>
    <p class="net">Net 32 FL OZ / 946 ML</p>
  </section>

</body>
</html>
```